Children, Youth, and Family Flyer

We need a flyer, 11 x 17, folded in half, double sided, to market our children, youth, and family ministries for the 2016-2017 school year. It will include our congregation's logo as well as logos that we have for a few of the programs. We also want it to have pictures (supplied). It needs to have a clean look and a children, youth, and family feel. I've included an assortment of pictures which can be used (certainly not all of them!). The brochure text is File 43.

Target Market(s)

Adults, families with children

Industry/Entity Type

Church

Font styles to use
Sans Serif

Requirements
Must have
• The information submitted in the brochure text document which is both in file 43 and also below. I want some photos. The church logo (file 40) must be on it.
• Children, Youth, and Family Ministries
• 2016-2017
• From infants through high-schoolers, Beacon Hollow has opportunities for children and youth of all ages to build their faith, engage with each other, and participate in experiences that will stay with them for a lifetime. We hope you will explore the ways in which you might become part of our community of faith.
• Pastor Rob Lensky, Associate Pastor – Children, Youth, and Family Ministries (RLensky@BeaconHollow.example).
• Rose Ellen Darby, Director of Faith Formation (REDarby@BeaconHollow.example ).
• 318 E. Marlow Ave., Fort Wayne, IN 46807
• (260) 555-0182 + BeaconHollow.example
• Working together to change the world through Jesus
• Children’s Ministries
• (ages 3 – grade 5)
• Sunday School
• Preschool students (ages 3, 4, and Pre-Kindergarten) meet in their specially appointed, self-contained classroom, Room 212W. Preschool students enjoy a Bible story, craft, snack, games, prayer, and a time for free play.
• Kindergarten through 5th grade students begin in Room 208W with activity centers where they choose what they'd like to do.  The opening follows where the day's Bible story is introduced.  Students then explore the story further through games, cooking, art, science, service, or in other ways.  
• Sundays at 10:00 am, beginning Sunday, September 18, 2016, through Sunday, May 21, 2017, except for holiday and school break weekends.
• Parenting in Faith, a weekly opportunity for discussion about parenting and issues of faith, meets at 10 am in Room 111W.
• Explorer Crew
• Held on Wednesday evenings (6:00 to 7:30 pm) for students in Kindergarten through grade 5. Explorer Crew begins with a kid-friendly dinner each week and then we have a great time with games, crafts, snack, stories, fun, and more!
• Explorer Crew is new this year and our first adventure will be held on Wednesday, September 14, 2016. We begin with dinner in Brennick Hall and then will move to the Youth Center.
• Family Nights
• Planned especially for families, Family Nights are held on Friday evenings and are an opportunity to share fellowship, expand your circle of friends at church, and grow in Christ as a family. A kid-friendly dinner is served along with a fun activity.
• September 23, 2016, 6 to 7:30 pm, Brixo Family Party
• November 18, 2016, 6 to 7:30 pm, Service Fair
• December 18, 2016, 6 to 7:30 pm, Los Posadas
• January 20, 2017, 6 to 7:30 pm, Indoor Miniature Golf
• March 10, 2017, 6 to 7:30 pm, Muffin Duels
• Middle and High School Ministries
• Confirmation
• Confirmation instruction at Beacon Hollow is for students in grades 6, 7, and 8. Confirmation provides students and their families an opportunity to grow closer to one another, to other Christians, and to God. It is about deepening faith, claiming our identity as children of God, growing evermore Christ-like, and reaching out in love and service to our neighbor.
• Junior High Huddle
• Our middle school youth group, called Junior High Huddle, brings middle school students together for fellowship, service, and fun. Friends are always welcome.
• High School
• Morning Circle
• Morning Circle is our weekly Sunday School class for middle and high school students. Morning Circle meets at 10:00 am on Sundays in Room 101W. Coffee, tea, hot chocolate, and donuts are served. Students share their highs and lows as well as what they are looking forward to. The discussion is often wide-ranging and sometimes a bit spirited!
• High School Youth Group
• High School Youth Group offers many opportunities that help us experience the fun of belonging with friends who are committed to each other and to God. We have fun with games, activities at church and elsewhere, Bible study, service, and much more. Our High School Youth Group meets most Sunday evenings from 5:30 to 7:30 pm.
• 2017 Mission Trip
• For students who have completed grade 6 through 12. Our destination this year is Big Lake, Alaska. The dates of the trip are July 7 through 17, 2017.
• Guild of St. Anselm
• The Guild of St. Anselm (usually called “GSA”) is Beacon Hollow’s group of outstanding mean and women who serve the congregation during worship.
• A group of Beacon Hollow GSA students and adult chaperones will attend the Great Server Gathering at the Kellbrook Memorial Basilica in Washington, DC, the weekend of October 7-9, 2016.
• Winter Weekend
• Join friends at Winter Weekend held this year at Beacon Hollow and the downtown Lantern Suites Inn the weekend of January 27-29, 2017. Harlow’s Lantern will be the band which performs and Ned Pilcraft will be our speaker. This will be the first time that Beacon Hollow hosts Winter Weekend for churches in our region.
• All Age Events
• Faith at Work
• Faith at Work is a cross-generational service opportunity. Meeting at 10 am in the Youth Center, people of all ages come together to make a difference in Jesus’ name. Some past projects include preparation of food for the Riverbend Shelter House, assembling college care packages for Beacon Hollow students away at college, sending cards to shut-ins, assembling “waiting room kits” for local hospitals, and many others.
• Everyone is welcome!
• Faith at Work will meet on the following Sundays: October 9, November 20, January 22, February 19, March 19, April 23.
• Blessing of the Animals
• Sunday, October 2, 2016, 3 pm
• An annual tradition, pets receive a blessing as we give thanks to God for the companionship and love our annuals provide. This will be held in Holm Chapel.
• Halloween Party
• Sunday, October 30, 3016, 5:00 to 7:00 pm
• Wear a costume and join us for dinner, games, and lots of candy!
• St. Nicholas Festival
• Sunday, December 11, 2016, 10 am
• Join us during the season of Advent as we remember St. Nicholas!
• Los Posadas
• Friday, December 16, 2016, 6 to 7:30 pm
• Join us as we travel with Mary and Joseph to the place where Jesus is born and we enjoy a Mexican fiesta complete with dinner and piñata!
• Ladle Drive of Giving
• Sunday, February 5, 2017, Noon
• Join us for a soup and salad lunch which raises money for Synod Food Relief, collects canned goods for Brookside Pantry, and prepares food for the Riverbend Shelter House.
• CocoaJam and Game Night
• Sunday, February 12, 2017, 5:00 to 7:00 pm
• All ages are invited for dinner, an evening of games, our chocolate fountain, and chocolate desserts!
• Snowrun Party
• Sunday, March 5, 2017, 5:00 to 7:00 pm
• Join us for dinner, games, and lots of fun as we immerse ourselves in the Snowrun!

```html
<!DOCTYPE html>
<html lang="en">
<head>
<meta charset="utf-8">
<title>Children, Youth and Family Ministries</title>
<link href="https://fonts.googleapis.com/css2?family=Raleway:wght@400;600;700;800;900&display=swap" rel="stylesheet">
<style>
:root{
  --teal:#1b7075;
  --rust:#c4472b;
  --ink:#262626;
  --lime:#a9c84b;
  --paper:#ffffff;
  --photo-a:#b9c7bf;
  --photo-b:#c9b9a8;
  --badge:#7a4a2a;
}
*{box-sizing:border-box;margin:0;padding:0}
html,body{width:1200px;height:775px;overflow:hidden;background:var(--paper)}
body{font-family:"Raleway",sans-serif;color:var(--ink);font-size:11.6px;line-height:14.6px}
.page{position:relative;width:1200px;height:775px}
.t{position:absolute;white-space:nowrap}
.r{text-align:right}
.banner{position:absolute;top:12px;height:48px;color:#fff;font-weight:900;font-size:44px;line-height:48px;letter-spacing:.5px;white-space:nowrap}
.banner--kids{left:0;width:592px;background:var(--teal);text-align:right;padding-right:8px}
.banner--youth{left:626px;width:574px;background:var(--rust);padding-left:4px}
.ages{top:62px;right:612px;color:var(--teal);font-weight:800;font-size:13px;line-height:16px}
.kids-head{color:var(--rust);font-weight:800;font-size:20px;line-height:24px}
.youth-head{color:var(--teal);font-weight:800;font-size:20px;line-height:24px;text-align:right}
.strong{font-weight:700}
.night-list{list-style:none;right:612px;top:549px;text-align:right;color:var(--rust);font-weight:800;font-size:14px;line-height:33.5px}
.photo{position:absolute;border-radius:50%}
.photo--team{left:443px;top:150px;width:188px;height:188px;border:9px solid var(--teal);background:linear-gradient(135deg,var(--photo-a),#dfe3dc 55%,#8e9c94)}
.photo--girls{left:0;top:548px;width:222px;height:222px;border:11px solid var(--lime);background:linear-gradient(160deg,var(--photo-b),#eadbd0 50%,#b08f7a)}
.badge-circle{position:absolute;left:1100px;top:250px;width:94px;height:94px;border-radius:50%;background:var(--badge);color:#fff;font-weight:800;font-size:13px;line-height:16px;display:flex;align-items:center;justify-content:center;text-align:center}
.guild-mark{position:absolute;left:1070px;top:590px;display:flex;align-items:center;gap:6px;color:var(--rust);font-weight:800;font-size:13px;line-height:15px}
.guild-mark .sq{width:16px;height:16px;background:var(--rust);flex:none}
</style>
</head>
<body>
<div class="page">
  <div class="banner banner--kids">CHILDREN’S MINISTRY</div>
  <div class="banner banner--youth">MIDDLE &amp; HIGH&nbsp; SCHOOL</div>
  <div class="t ages">AGES 3 - GRADE 5</div>

  <div class="photo photo--team" role="img" aria-label="Photo of youth leaders and students in matching event T-shirts"></div>
  <div class="photo photo--girls" role="img" aria-label="Photo of two young girls smiling at a family event"></div>

  <h2 class="t kids-head" style="left:24px;top:71px">Sunday School</h2>
  <p class="t" style="left:24px;top:98px">Preschool students (ages 3, 4, and Pre-Kindergarten) meet in their specially appointed,<br>self-contained classroom, Room 212W.&nbsp; Preschool students enjoy a Bible story, craft, snack, games,<br>prayer, and a time for free play.</p>
  <p class="t" style="left:24px;top:155px">Kindergarten through 5th grade students begin in Room 208W with activity<br>centers where they choose what they’d like to do.&nbsp; The opening follows<br>where the day’s Bible story is introduced.&nbsp; Students then explore the story<br>further through games, cooking, art, science, service, or in other ways.</p>
  <p class="t" style="left:24px;top:227px">Sundays at 10:00 am, beginning Sunday, September 18, 2016, through<br>Sunday, May 21, 2017, except for holiday and school break weekends.</p>
  <p class="t strong" style="left:24px;top:269px">Parenting in Faith, a weekly opportunity for discussion about<br>parenting and issues of faith, meets at 10 am in Room 111W.</p>

  <h2 class="t kids-head" style="left:24px;top:316px">Explorer Crew</h2>
  <p class="t" style="left:24px;top:343px">Held on Wednesday evenings (6:00 to 7:30 pm) for students in Kindergarten through<br>grade 5.&nbsp; Explorer Crew begins with a kid-friendly dinner each week and then we<br>have a great time with games, crafts, snack, stories, fun, and more!</p>
  <p class="t" style="left:24px;top:400px">Explorer Crew is new this year and our first adventure will be held on Wednesday, September 14,<br>2016.&nbsp; We begin with dinner in Brennick Hall and then will move to the Youth Center.</p>

  <h2 class="t kids-head" style="left:24px;top:444px">Family Nights</h2>
  <p class="t" style="left:24px;top:471px">Planned especially for families, Family Nights are held on Friday evenings and are an opportunity to<br>share fellowship, expand your circle of friends at church, and grow in Christ as a family.</p>
  <p class="t" style="left:24px;top:514px">A kid-friendly dinner is served along with a fun activity.</p>

  <ul class="t night-list">
    <li>September 23, 2016, 6 to 7:30 pm, Brixo Family Party</li>
    <li>November 18, 2016, 6 to 7:30 pm, Service Fair</li>
    <li>December 18, 2016, 6 to 7:30 pm, Los Posadas</li>
    <li>January 20, 2017, 6 to 7:30 pm, Indoor Miniature Golf</li>
    <li>March 10, 2017, 6 to 7:30 pm, Muffin Duels</li>
  </ul>

  <h2 class="t youth-head" style="right:8px;top:71px">Confirmation</h2>
  <p class="t r" style="right:8px;top:98px">Confirmation instruction at Beacon Hollow is for students in grades 6, 7, and 8.&nbsp; Confirmation provides<br>students and their families an opportunity to grow closer to one another, to other Christians, and to God.<br>It is about deepening faith, claiming our identity as children of God, growing evermore Christ-like, and<br>reaching out in love and service to our neighbor.</p>

  <h2 class="t youth-head" style="right:8px;top:169px">Junior High Huddle</h2>
  <p class="t r" style="right:8px;top:195px">Our middle school youth group, called Junior High Huddle,<br>brings middle school students together for fellowship, service, and fun.<br>Friends are always welcome</p>

  <h2 class="t youth-head" style="right:110px;top:249px">Morning Circle</h2>
  <p class="t r" style="right:110px;top:276px">Morning Circle is our weekly Sunday School class for middle and high school<br>students.&nbsp; Morning Circle meets at 10:00 am on Sundays in Room 101W.<br>Coffee, tea, hot chocolate, and donuts are served.&nbsp; Students share their highs<br>and lows as well as what they are looking forward to. The discussion is often<br>wide-ranging and sometimes a bit spirited!</p>
  <div class="badge-circle">Morning<br>Circle</div>

  <h2 class="t youth-head" style="right:8px;top:352px">High School Youth Group</h2>
  <p class="t r" style="right:8px;top:378px">High School Youth Group offers many opportunities that help us experience the fun of belonging<br>with friends who are committed to each other and to God.&nbsp; We have fun with games, activities at<br>church and elsewhere, Bible study, service, and much more.<br><span class="strong">Our High School Youth Group meets most Sunday evenings from 5:30 to 7:30 pm.</span></p>

  <h2 class="t youth-head" style="right:8px;top:453px">2017 Mission Trip</h2>
  <p class="t r" style="right:8px;top:480px">For students who have completed grade 6 through 12.&nbsp; Our destination this year is Big Lake, Alaska.&nbsp; The<br>dates of the trip are July 7 through 17, 2017. We will have a positive, Christ-centered impact on the<br>community as we serve in a variety of settings, from outreach to elderly residents, to work projects and<br>partnerships with local social service organizations.</p>

  <h2 class="t youth-head" style="right:140px;top:555px">Guild of St. Anselm</h2>
  <p class="t r" style="right:140px;top:582px">The Guild of St. Anselm (usually called “GSA”) is Beacon Hollow’s group of<br>outstanding mean and women who serve the congregation during<br>worship. A group of Beacon Hollow GSA students and adult chaperones<br>will attend the Great Server Gathering at the Kellbrook Memorial<br>Basilica in Washington, DC, the weekend of October 7-9, 2016.</p>
  <div class="guild-mark"><span class="sq"></span><span>Guild of<br>St. Anselm</span></div>

  <h2 class="t youth-head" style="right:8px;top:671px">Winter Weekend</h2>
  <p class="t r" style="right:8px;top:693px">Join friends at Winter Weekend held this year at Beacon Hollow and the downtown Lantern Suites Inn<br>the weekend of January 27-29, 2017.&nbsp; Harlow’s Lantern will be the band which performs and<br>Ned Pilcraft will be our speaker.&nbsp; This will be the first time that Beacon Hollow hosts<br>Winter Weekend for churches in our region.</p>
</div>
</body>
</html>
```